business card design for a plumbing contractor

i need a double business card for a plumbing business, our initial service is residential Sewer Drain Cleaning.

Target Market(s)

other plumbing Business

Industry/Entity Type

Plumbing

Contact Information for Business Card

www.PipeworksCrestline.example- 5817302946-

Font styles to use
Serif

Colors
ec1f27
0455a3

```html
<!DOCTYPE html>
<html lang="en">
<head>
<meta charset="utf-8">
<title>Pipeworks Crestline – Business Card</title>
<link rel="stylesheet" href="https://fonts.googleapis.com/css2?family=Arimo:wght@400;700&family=PT+Serif&display=swap">
<style>
  :root {
    --stage: #2b2b2d;
    --card: #f7f7f7;
    --red: #ec1f27;
    --blue: #0455a3;
    --grey: #7a746b;
    --ink: #1d1d1d;
    --mark-faint: rgba(236, 31, 39, 0.07);
  }
  html, body {
    margin: 0;
    width: 1200px;
    height: 997px;
    overflow: hidden;
    background: var(--stage);
  }
  .card {
    position: absolute;
    width: 600px;
    height: 343px;
    background: var(--card);
    border-radius: 22px;
    overflow: hidden;
    font-family: "Arimo", Arial, sans-serif;
  }
  .card-front { left: 70px; top: 90px; }
  .card-back { left: 530px; top: 520px; }
  .card-bands {
    position: absolute;
    inset: 0;
    width: 600px;
    height: 343px;
  }
  .wordmark {
    position: absolute;
    font-family: "Arimo", Arial, sans-serif;
    font-weight: 700;
    color: var(--grey);
    line-height: 0.95;
    margin: 0;
  }
  .card-front .wordmark {
    left: 150px;
    top: 118px;
    font-size: 46px;
  }
  .card-back .wordmark {
    right: 40px;
    top: 30px;
    font-size: 28px;
    text-align: right;
  }
  .wordmark-dot {
    display: inline-block;
    width: 0.42em;
    height: 0.42em;
    border-radius: 50%;
    background: var(--red);
    margin-left: 0.18em;
    vertical-align: middle;
  }
  .faint-mark {
    position: absolute;
    right: 60px;
    top: 90px;
    width: 200px;
    height: 200px;
    border-radius: 50%;
    background: var(--mark-faint);
  }
  .holder {
    position: absolute;
    left: 36px;
    top: 112px;
  }
  .holder-name {
    margin: 0;
    color: var(--red);
    font-weight: 700;
    font-size: 17px;
    letter-spacing: 0.5px;
    text-transform: uppercase;
  }
  .holder-title {
    margin: 2px 0 0;
    color: var(--blue);
    font-size: 13px;
  }
  .services {
    position: absolute;
    right: 40px;
    top: 165px;
    margin: 0;
    padding: 0;
    list-style: none;
    text-align: right;
    font-family: "PT Serif", Georgia, serif;
    font-variant: small-caps;
    color: var(--red);
    font-size: 15px;
    line-height: 1.75;
  }
  .contact-tab {
    position: absolute;
    left: 0;
    top: 196px;
    width: 30px;
    height: 96px;
  }
  .contacts {
    position: absolute;
    left: 46px;
    top: 200px;
    margin: 0;
    padding: 0;
    list-style: none;
    font-size: 15px;
    color: var(--ink);
    line-height: 28px;
  }
</style>
</head>
<body>

<section class="card card-front" aria-label="Card front">
  <svg class="card-bands" viewBox="0 0 600 343" aria-hidden="true">
    <path d="M0 343 L0 331 L452 321 C464 321 470 330 472 343 Z" fill="var(--red)"/>
    <path d="M458 343 C468 320 488 314 520 313 L600 309 L600 343 Z" fill="var(--blue)"/>
  </svg>
  <h1 class="wordmark">Pipeworks<br>Crestline<span class="wordmark-dot"></span></h1>
</section>

<section class="card card-back" aria-label="Card back">
  <div class="faint-mark" aria-hidden="true"></div>
  <svg class="card-bands" viewBox="0 0 600 343" aria-hidden="true">
    <path d="M0 343 L0 331 L452 321 C464 321 470 330 472 343 Z" fill="var(--red)"/>
    <path d="M458 343 C468 320 488 314 520 313 L600 309 L600 343 Z" fill="var(--blue)"/>
  </svg>
  <h2 class="wordmark">Pipeworks<br>Crestline<span class="wordmark-dot"></span></h2>

  <div class="holder">
    <p class="holder-name">Dana Whitlock</p>
    <p class="holder-title">Director</p>
  </div>

  <ul class="services">
    <li>Sewer Drain Cleaning</li>
    <li>Maintenance</li>
    <li>Trenchless Pipe Installs</li>
  </ul>

  <svg class="contact-tab" viewBox="0 0 30 96" aria-hidden="true">
    <path d="M0 0 H22 A8 8 0 0 1 30 8 V88 A8 8 0 0 1 22 96 H0 Z" fill="var(--blue)"/>
    <rect x="10" y="12" width="9" height="15" rx="2" fill="none" stroke="#fff" stroke-width="1.6"/>
    <rect x="8" y="42" width="14" height="10" rx="1" fill="none" stroke="#fff" stroke-width="1.6"/>
    <path d="M8 43 L15 48 L22 43" fill="none" stroke="#fff" stroke-width="1.4"/>
    <path d="M15 84 C10 77 9 75 9 72 A6 6 0 0 1 21 72 C21 75 20 77 15 84 Z" fill="#fff"/>
    <circle cx="15" cy="72" r="2.2" fill="var(--blue)"/>
  </svg>

  <ul class="contacts">
    <li>5817302946</li>
    <li>Dispatcher@PipeworksCrestline.example</li>
    <li>www.PipeworksCrestline.example</li>
  </ul>
</section>

</body>
</html>
```